Business card for IT company

Looking for a business card for an IT company providing server, network, and application support to medium businesses. Company name is Calderwick Systems. Website is www.calderwicksystems.example, would like to use the green color that is on the homepage. Prefer design to be done in Illustrator. Please, only DESIGNERS apply - no PHP programmers attempting to do design. Thank you

Industry/Entity Type

Information Technology

Requirements
Must have
• Green
Should not have
• Template designs, or designs done by non-designer type people

```html
<!DOCTYPE html>
<html lang="en">
<head>
<meta charset="utf-8">
<title>Calderwick Systems – Business Card</title>
<link href="https://fonts.googleapis.com/css2?family=Open+Sans:wght@400;600&display=swap" rel="stylesheet">
<style>
  :root {
    --canvas-bg: #0e1019;
    --green-light: #3cb24b;
    --green-mid: #2a9744;
    --green-dark: #1a7a3c;
    --ink: #ffffff;
  }
  * { box-sizing: border-box; margin: 0; padding: 0; }
  html, body {
    width: 1200px; height: 1000px; overflow: hidden;
    background: var(--canvas-bg);
    font-family: "Open Sans", Arial, sans-serif;
    color: var(--ink);
  }
  .canvas {
    position: relative; width: 1200px; height: 1000px;
  }
  .card {
    position: absolute; top: 350px;
    width: 500px; height: 286px;
    background: radial-gradient(circle at 22% 28%, var(--green-light) 0%, var(--green-mid) 45%, var(--green-dark) 100%);
    box-shadow: 0 6px 0 #176e35, 0 18px 30px rgba(0,0,0,.55);
    overflow: hidden;
  }
  .card--front { left: 70px; }
  .card--back  { left: 630px; }

  .card__frame { position: absolute; inset: 0; }

  .brand {
    position: absolute; display: flex; flex-direction: column; align-items: center;
  }
  .brand__mark {
    width: 54px; height: 54px; border-radius: 50%; background: var(--ink);
  }
  .brand__name {
    margin-top: 8px; font-size: 13px; font-weight: 400; letter-spacing: 1.5px;
    text-transform: uppercase; white-space: nowrap;
  }
  .card--front .brand { left: 28px; top: 38px; }
  .card--back .brand { left: 50%; top: 50%; transform: translate(-50%, -50%); }
  .card--back .brand__mark { width: 62px; height: 62px; }

  .holder {
    position: absolute; right: 118px; top: 40px; text-align: right;
    font-size: 11px; line-height: 15px;
  }

  .contacts {
    position: absolute; left: 40px; top: 196px; list-style: none;
    font-size: 12px;
  }
  .contacts li { display: flex; align-items: center; gap: 7px; height: 22px; }
  .contacts .icon {
    width: 16px; height: 16px; border-radius: 50%; background: var(--ink);
    display: flex; align-items: center; justify-content: center;
  }
  .contacts .icon svg { width: 10px; height: 10px; }
</style>
</head>
<body>
<main class="canvas">

  <section class="card card--front" aria-label="Business card front">
    <svg class="card__frame" viewBox="0 0 500 286" fill="none" stroke="#ffffff" stroke-width="1.4">
      <polyline points="0,8 52,8 52,20 392,20 392,0"/>
      <polyline points="392,20 392,205 500,205"/>
      <polyline points="408,0 408,220 500,220"/>
      <polyline points="150,118 376,118 376,232 500,232"/>
      <polyline points="0,170 118,170 118,154"/>
    </svg>

    <div class="brand">
      <div class="brand__mark"></div>
      <span class="brand__name">Calderwick Systems</span>
    </div>

    <p class="holder">Name: xxxxxxxxxxxxx<br>xxxxxxxx</p>

    <ul class="contacts">
      <li>
        <span class="icon"><svg viewBox="0 0 10 10"><path d="M2 1 L3.6 1 L4.2 3 L3.2 3.8 Q4.2 5.8 6.2 6.8 L7 5.8 L9 6.4 L9 8 Q8.6 9 7.6 9 Q1 8.4 1 2.4 Q1 1.4 2 1Z" fill="#2a9744"/></svg></span>
        555.014.0172
      </li>
      <li>
        <span class="icon"><svg viewBox="0 0 10 10"><rect x="1" y="2.5" width="8" height="5.5" fill="#2a9744"/><polyline points="1,2.5 5,5.6 9,2.5" stroke="#fff" stroke-width="0.8" fill="none"/></svg></span>
        support@calderwicksystems.example
      </li>
      <li>
        <span class="icon"><svg viewBox="0 0 10 10" fill="none" stroke="#2a9744" stroke-width="1"><circle cx="5" cy="5" r="4"/><ellipse cx="5" cy="5" rx="1.8" ry="4"/><line x1="1" y1="5" x2="9" y2="5"/></svg></span>
        www.calderwicksystems.example
      </li>
    </ul>
  </section>

  <section class="card card--back" aria-label="Business card back">
    <div class="brand">
      <div class="brand__mark"></div>
      <span class="brand__name">Calderwick Systems</span>
    </div>
  </section>

</main>
</body>
</html>
```